Business card for my company-RMK Design Studio

I do not have a logo-I like red and keeping it clean. Information that should be on the card:
Tom Brakefield AIA
Architecture Planning Interiors
Cell Phone-614.492.5068
email-rmkarchitect1@lunvale.com
www.rmkdesignstudio.net

```html
<!DOCTYPE html>
<html lang="en">
<head>
<meta charset="utf-8">
<title>RMK Design Studio – Business Card</title>
<link rel="stylesheet" href="https://fonts.googleapis.com/css2?family=Poppins:wght@600&family=Roboto:wght@400&display=swap">
<style>
  :root {
    --brand-red: #e80000;
    --card-white: #ffffff;
    --disc-grey: #ececec;
    --page-bg: #f1f1f1;
  }
  * { margin: 0; padding: 0; box-sizing: border-box; }
  html, body {
    width: 1200px;
    height: 900px;
    overflow: hidden;
    background: var(--page-bg);
  }
  .business-card {
    position: absolute;
    left: 100px;
    top: 141px;
    width: 1000px;
    height: 618px;
    background: var(--brand-red);
    color: var(--card-white);
    overflow: hidden;
  }
  .identity {
    position: absolute;
    left: 47px;
    top: 80px;
  }
  .identity__name {
    font-family: "Poppins", sans-serif;
    font-weight: 600;
    font-size: 36px;
    line-height: 1.05;
    letter-spacing: 0.3px;
  }
  .identity__disciplines {
    font-family: "Roboto", sans-serif;
    font-weight: 400;
    font-size: 29px;
    line-height: 1.1;
    letter-spacing: 0.2px;
  }
  .contact-list {
    position: absolute;
    left: 47px;
    top: 440px;
    list-style: none;
    font-family: "Roboto", sans-serif;
    font-size: 30px;
    line-height: 37px;
  }
  .contact-list__item {
    display: flex;
    align-items: center;
    gap: 10px;
  }
  .contact-list__icon {
    width: 26px;
    height: 26px;
    flex: none;
  }
  .brand-disc {
    position: absolute;
    left: 413px;
    top: 42px;
    width: 532px;
    height: 532px;
    border-radius: 50%;
    background: var(--disc-grey);
    display: flex;
    align-items: center;
    justify-content: center;
  }
  .brand-disc__name {
    color: var(--brand-red);
    font-family: "Poppins", sans-serif;
    font-weight: 600;
    font-size: 38px;
    line-height: 1.2;
    text-align: center;
  }
</style>
</head>
<body>
  <main class="business-card">
    <header class="identity">
      <h1 class="identity__name">TOM BRAKEFIELD AIA</h1>
      <p class="identity__disciplines">Architecture Planning Interiors</p>
    </header>

    <ul class="contact-list">
      <li class="contact-list__item">
        <svg class="contact-list__icon" viewBox="0 0 26 26" aria-hidden="true">
          <rect x="5" y="1.5" width="16" height="23" rx="2.5" fill="none" stroke="#fff" stroke-width="2.2"/>
          <line x1="5" y1="19" x2="21" y2="19" stroke="#fff" stroke-width="2"/>
          <circle cx="13" cy="21.6" r="1.3" fill="#fff"/>
        </svg>
        <span>614.492.5068</span>
      </li>
      <li class="contact-list__item">
        <svg class="contact-list__icon" viewBox="0 0 26 26" aria-hidden="true">
          <rect x="1" y="5" width="24" height="16" fill="#fff"/>
          <polyline points="1,5 13,15 25,5" fill="none" stroke="#e80000" stroke-width="2"/>
          <line x1="1" y1="21" x2="10" y2="13" stroke="#e80000" stroke-width="1.6"/>
          <line x1="25" y1="21" x2="16" y2="13" stroke="#e80000" stroke-width="1.6"/>
        </svg>
        <span>rmkarchitect1@lunvale.com</span>
      </li>
      <li class="contact-list__item">
        <svg class="contact-list__icon" viewBox="0 0 26 26" aria-hidden="true" fill="none" stroke="#fff" stroke-width="1.8">
          <circle cx="13" cy="13" r="11.5"/>
          <ellipse cx="13" cy="13" rx="5" ry="11.5"/>
          <line x1="1.5" y1="13" x2="24.5" y2="13"/>
          <path d="M3.5 7h19M3.5 19h19"/>
        </svg>
        <span>www.rmkdesignstudio.net</span>
      </li>
    </ul>

    <div class="brand-disc">
      <p class="brand-disc__name">RMK Design Studio</p>
    </div>
  </main>
</body>
</html>
```